依頼詳細
最低限の要件としては、下記のみとなりますが、
少しでも大学生・大学院生の応募が増えるようにセンスのあるチラシを作成したいと考えております。

■要件内容
①赤を基調とすること(赤色は昨年のチラシ、パンフ等で用いたテーマカラーです)
②昨年のイベントと同じことを示すため、KSTFおよびCampus Startup Flagship Cup という名称の使用
記載項目
・昨年のイベントと同じことを示すため、KSTFおよびCampus Startup Flagship Cup 2013という名称の使用

・記載する文字量は昨年のチラシとほぼ同様です。
現在調整中の内容が多く、情報が分かり次第、本募集へ追記、または当選となるデザインのご作成者様とのやりとりで、具体的文言を入れて頂くかたちをとらせて頂ければと思います。
サイズ
A4
ページ数
両面
希望イメージ
シンプル 複雑
単色 カラフル
暗い 明るい
日常 高級
遊び心 厳粛
未来的 伝統的
女性的 男性的
希望する色
赤を基調にして作成を御願い致します。
納品ファイル
• イラストレーター形式 (.ai)
補足説明
※去年のチラシを添付しておりますので、ご確認の上、作成をお願いいたします。
昨年チラシが添付漏れておりましたので、添付致します。
ご確認の上、作成をお願い致します。

壁をも壊しながら突き進む学生らしい躍動感が感じられ、大変気に入りました。よろしくお願いいたします。

皆様、多くのご応募大変ありがとうございました。よい提案がたくさんありまして、非常に迷いました。
今後ともどうぞよろしくお願いいたします。

```html
<!DOCTYPE html>
<html lang="ja">
<head>
<meta charset="utf-8">
<title>KSTF 2013 ビジネスプランコンテスト全国大会</title>
<link rel="stylesheet" href="https://fonts.googleapis.com/css2?family=Cinzel:wght@500;700&family=Cormorant+Garamond:wght@500;600&family=Noto+Serif+JP:wght@500&family=Noto+Sans+JP:wght@400;500&display=swap">
<style>
  :root {
    --red-deep: #8e0a1c;
    --red-main: #c8142c;
    --red-bright: #e2283f;
    --white: #ffffff;
    --gold-light: #ecd49c;
    --gold-mid: #c9a767;
    --gold-dark: #9c7a40;
  }
  html, body { margin: 0; padding: 0; overflow: hidden; background: #e9e9e9; }
  .flyer {
    position: relative;
    width: 849px; height: 1200px;
    overflow: hidden;
    color: var(--white);
    background: var(--red-main);
  }
  .flyer-backdrop {
    position: absolute; inset: 0;
    background:
      radial-gradient(ellipse 60% 45% at 65% 38%, var(--red-bright) 0%, transparent 70%),
      radial-gradient(ellipse 70% 50% at 20% 80%, rgba(142,10,28,.55) 0%, transparent 70%),
      linear-gradient(160deg, var(--red-main) 0%, var(--red-bright) 45%, var(--red-deep) 100%);
  }
  .event-name {
    position: absolute; left: 40px; top: 28px; margin: 0;
    font-family: "Cormorant Garamond", serif; font-weight: 600;
    font-size: 46px; line-height: 45px; letter-spacing: .5px;
  }
  .event-name span { display: block; }
  .tagline {
    position: absolute; left: 428px; top: 196px; margin: 0;
    font-family: "Noto Serif JP", serif; font-weight: 500;
    font-size: 22px; letter-spacing: 2px;
  }
  .acronym {
    position: absolute; left: 418px; top: 222px; margin: 0;
    font-family: "Cinzel", serif; font-weight: 500;
    font-size: 172px; line-height: 1; letter-spacing: 4px;
    background: linear-gradient(180deg, var(--gold-light) 0%, var(--gold-mid) 50%, var(--gold-dark) 100%);
    -webkit-background-clip: text; background-clip: text; color: transparent;
  }
  .event-info { position: absolute; left: 270px; top: 712px; right: 40px; }
  .event-date, .event-venue {
    margin: 0; font-family: "Cormorant Garamond", serif; font-weight: 600;
    font-size: 34px; line-height: 44px; letter-spacing: 1px;
  }
  .event-title {
    margin: 6px 0 10px; font-family: "Noto Sans JP", sans-serif; font-weight: 500;
    font-size: 20px; letter-spacing: 1px;
  }
  .event-details, .organizers {
    margin: 0; padding: 0; list-style: none;
    font-family: "Noto Sans JP", sans-serif; font-weight: 400;
    font-size: 11.5px; line-height: 19px;
  }
  .event-details dt { display: inline; font-weight: 500; }
  .event-details dd { display: inline; margin: 0; }
  .organizers { position: absolute; left: 40px; top: 995px; right: 40px; font-size: 11px; line-height: 20px; }
</style>
</head>
<body>
<main class="flyer">
  <div class="flyer-backdrop" role="img" aria-label="赤い多角形の破片が重なり合う幾何学的な背景"></div>

  <h1 class="event-name">
    <span>Campus</span><span>Startup</span><span>Flagship</span><span>Cup 2013</span>
  </h1>
  <p class="tagline">分析と閃きを ビジネスへ昇華しろ。</p>
  <p class="acronym">KSTF</p>

  <section class="event-info">
    <p class="event-date">8th Decemeber 2013</p>
    <p class="event-venue">MIYAMA HALL</p>
    <p class="event-title">ビジネスプランコンテスト全国大会 2013</p>
    <dl class="event-details">
      <div><dt>開催日時：</dt><dd>平成25年12月7日（土）13:00～（コンテスト等）18:30～（懇親会）</dd></div>
      <div><dt>開催場所：</dt><dd>東都大学 深山ホール（東京都文京区本郷）</dd></div>
      <div><dt>プラン締切：</dt><dd>11月14日（木）・一般参加申込締切 11月29日（金）</dd></div>
    </dl>
  </section>

  <ul class="organizers">
    <li>主催：大学起業教育推進ネットワーク ／ 産業振興庁</li>
    <li>共催：東都大学産学連携本部 ／ 学術振興庁</li>
    <li>後援：新興企業支援協会 ／ 若手起業家育成機構 ／ 地域創業推進会議 ／ 学生事業研究会</li>
    <li>協賛：未来創業基金 ／ 青葉ベンチャー協議会（ABC）</li>
    <li>お問合せ：産業振興庁 新規産業室　TEL：03.0000.4821</li>
  </ul>
</main>
</body>
</html>
```